Business Card Design Project

for a second hand vintage clothing store. shop name is The Velvet Cupboard

Cards to be double sided

The name on the card is Joanna Whitfield

Information to put on card:

The Velvet Cupboard
Joanna Whitfield (no job title)
42/871 Dunmore St, Glenwick, Sydney, NSW, 2009.
Mobile: 0412 905 261
Email: thevelvetcupboard@mailbox.com.au
Web: www.thevelvetcupboard.com.au

Target Market(s)

Women looking at vintage clothing

Industry/Entity Type

Clothing

```html
<!DOCTYPE html>
<html lang="en">
<head>
<meta charset="utf-8">
<title>The Velvet Cupboard – Business Card</title>
<link rel="stylesheet" href="https://fonts.googleapis.com/css2?family=Pinyon+Script&family=Arimo:wght@400;700&display=swap">
<style>
  :root {
    --backdrop: #1c1c1e;
    --plum: #4f1f31;
    --plum-deep: #3f1827;
    --amber: #d98a22;
    --cream: #ecdcae;
    --cream-soft: #f3e3bd;
    --ink: #4a1b2c;
    --script: "Pinyon Script", cursive;
    --sans: "Arimo", Arial, sans-serif;
  }
  * { box-sizing: border-box; margin: 0; padding: 0; }
  html, body { width: 1200px; height: 984px; overflow: hidden; }
  body {
    background: var(--backdrop);
    font-family: var(--sans);
    display: flex;
    flex-direction: column;
    align-items: center;
    justify-content: center;
    gap: 40px;
  }
  .card {
    position: relative;
    width: 760px;
    height: 434px;
    border-radius: 30px;
    overflow: hidden;
    background: var(--amber);
    box-shadow: 0 14px 36px rgba(0,0,0,.55);
  }
  .card__shape { position: absolute; inset: 0; width: 100%; height: 100%; }

  .wordmark {
    position: absolute;
    font-family: var(--script);
    color: var(--cream);
    font-weight: 400;
    white-space: nowrap;
    line-height: 1;
  }
  .card--front .wordmark {
    left: 0; right: 0; top: 112px;
    text-align: center;
    font-size: 80px;
  }
  .card--front .web {
    position: absolute;
    right: 44px; bottom: 24px;
    font-size: 19px;
    color: var(--ink);
    letter-spacing: .3px;
  }

  .card--back .wordmark {
    left: 250px; top: 40px;
    font-size: 58px;
  }
  .person {
    position: absolute;
    left: 0; right: 0; top: 200px;
    text-align: center;
  }
  .person__name {
    font-family: var(--script);
    font-size: 52px;
    color: var(--ink);
    line-height: 1.1;
  }
  .address {
    position: absolute;
    left: 44px; top: 296px;
    display: flex;
    gap: 16px;
    font-size: 16px;
    line-height: 1.3;
  }
  .label { font-weight: 700; color: var(--ink); }
  .value { color: var(--cream-soft); }
  .contacts {
    position: absolute;
    left: 350px; top: 316px;
    display: grid;
    grid-template-columns: auto auto;
    column-gap: 16px;
    row-gap: 3px;
    font-size: 16px;
    line-height: 1.3;
  }
  .contacts .label { text-align: right; }
</style>
</head>
<body>

  <section class="card card--front" aria-label="Card front">
    <svg class="card__shape" viewBox="0 0 760 434" preserveAspectRatio="none" aria-hidden="true">
      <path d="M0 0 H760 V338 Q560 352 380 368 T0 392 Z" fill="var(--plum)"/>
      <path d="M0 392 Q200 384 380 368 T760 338" fill="none" stroke="var(--plum-deep)" stroke-width="3"/>
    </svg>
    <h1 class="wordmark">The Velvet Cupboard</h1>
    <p class="web">www.thevelvetcupboard.com.au</p>
  </section>

  <section class="card card--back" aria-label="Card back">
    <svg class="card__shape" viewBox="0 0 760 434" preserveAspectRatio="none" aria-hidden="true">
      <path d="M0 0 H760 V170 Q600 162 470 156 L455 166 L442 154 Q200 146 0 140 Z" fill="var(--plum)"/>
      <path d="M0 140 Q200 146 442 154 L455 166 L470 156 Q600 162 760 170" fill="none" stroke="var(--plum-deep)" stroke-width="3"/>
      <line x1="36" y1="176" x2="724" y2="188" stroke="var(--ink)" stroke-width="1.6" stroke-dasharray="6 6"/>
    </svg>
    <h1 class="wordmark">The Velvet Cupboard</h1>

    <div class="person">
      <p class="person__name">Joanna Whitfield</p>
    </div>

    <div class="address">
      <span class="label">Address:</span>
      <span class="value">42/871 Dunmore St<br>Glenwick, Sydney<br>NSW<br>2009</span>
    </div>

    <div class="contacts">
      <span class="label">Mobile:</span><span class="value">0412 905 261</span>
      <span class="label">Email:</span><span class="value">thevelvetcupboard@mailbox.com.au</span>
      <span class="label">Web:</span><span class="value">www.thevelvetcupboard.com.au</span>
    </div>
  </section>

</body>
</html>
```